Convert my PowerPoint mock up of a hiring process flow to simple, informative illustration with some

I need to create an illustration which is meant to be an overview of a hiring process for a medical training start up. I created a pretty rough PowerPoint mock up that hopefully shows what I am trying to do. My hope is that I would get the illustration created and can add it to my website. I have several other similar projects needed as well and probably ongoing graphic design work if we develop a good working relationship.

Site: www.brindlecare.com

Target Market(s)

Medical employers

Industry/Entity Type

Healthcare

Number of Pages Required

1 page

Font styles to use
Serif
Sans Serif

Colors
2fb6a2
85cae6

Requirements
Must have
• Simple illustration when done
Nice to have
• Fits very well with existing look and feel of site.
Should not have
• Not sure

```html
<!DOCTYPE html>
<html lang="en">
<head>
<meta charset="utf-8">
<title>BrindleCare – Hiring Process</title>
<link href="https://fonts.googleapis.com/css2?family=Montserrat:wght@300;400;500&family=Open+Sans:wght@400;600&display=swap" rel="stylesheet">
<style>
  :root{
    --teal:#2fb6a2;
    --teal-soft:#3cbfa9;
    --sky:#85cae6;
    --sky-hero:#a9dbee;
    --sky-band:#8fcfe8;
    --ink:#333333;
    --dark:#2e2e2e;
    --grey:#555555;
    --name:#4a4a4a;
    --white:#ffffff;
  }
  *{box-sizing:border-box;margin:0;padding:0}
  html,body{width:1200px;height:3462px;overflow:hidden;background:var(--white)}
  body{font-family:"Open Sans",Arial,sans-serif;color:var(--ink);position:relative}
  .section{position:absolute;left:0;width:1200px}
  .heading{font-family:"Montserrat",Arial,sans-serif;font-weight:300;text-align:center;position:absolute;left:0;width:1200px}
  .btn{position:absolute;display:flex;align-items:center;justify-content:center;font-family:"Open Sans",Arial,sans-serif;font-size:13px;letter-spacing:.5px;color:var(--white);text-transform:uppercase}

  /* header */
  .site-header{top:0;height:104px;background:var(--white)}
  .brand{position:absolute;left:127px;top:34px;display:flex;align-items:center;gap:10px;font-family:"Montserrat",Arial,sans-serif;font-weight:500;font-size:24px;color:#1c4f8c}
  .brand-square{width:30px;height:30px;background:#1c4f8c}
  .menu-icon{position:absolute;left:1045px;top:40px}

  /* hero */
  .hero{top:104px;height:438px;background:linear-gradient(180deg,#b4e0f1,var(--sky-hero))}
  .hero-title{position:absolute;left:162px;top:110px;font-family:"Montserrat",Arial,sans-serif;font-weight:300;font-size:64px;color:var(--white)}
  .hero-text{position:absolute;left:162px;top:212px;width:360px;font-size:12px;line-height:18px;color:var(--white)}
  .hero .btn{left:162px;top:284px;width:143px;height:41px;background:var(--teal)}
  .hero-art{position:absolute;left:612px;top:76px;width:396px;height:293px;border-radius:8px;background:linear-gradient(135deg,#d7eef7,#9fd3e8)}
  .dots{position:absolute;left:164px;top:397px;display:flex;gap:9px}
  .dots span{width:12px;height:12px;border-radius:50%;background:var(--white)}
  .dots span:first-child{background:#9db4bd}

  /* candidate rows */
  .people{position:absolute;display:flex;gap:11px}
  .person{width:180px;text-align:center}
  .photo{width:180px;height:166px;background:linear-gradient(160deg,#c9ccd2,#6d7683)}
  .person-name{margin-top:25px;font-size:15px;color:var(--name)}

  .pool{top:542px;height:450px;background:var(--teal)}
  .pool .people{left:129px;top:46px}
  .pool .person-name{color:var(--white)}
  .pool .heading{top:306px;font-size:38px;line-height:46px;color:var(--white);font-weight:400}

  .summary{top:992px;height:443px;background:var(--dark)}
  .summary-art{position:absolute;inset:0;background:radial-gradient(ellipse at 50% 55%,#3b3b3b,#2a2a2a 75%)}
  .summary .heading{top:108px;font-size:38px;color:var(--white);font-weight:400}
  .summary-text{position:absolute;left:200px;top:196px;width:850px;text-align:center;font-size:17.5px;line-height:31px;color:var(--white)}
  .summary .btn{left:531px;top:349px;width:138px;height:39px;background:var(--sky)}

  .selection{top:1435px;height:462px;background:var(--white)}
  .selection .heading{top:58px;font-size:38px;line-height:48px;color:var(--grey)}
  .selection .people{left:129px;top:197px}

  .band{height:212px}
  .band-art{position:absolute;inset:0}
  .band .heading{top:82px;font-size:40px;color:var(--white);font-weight:400}
  .protocol{top:1897px;background:var(--teal-soft)}
  .protocol .band-art{background:linear-gradient(90deg,#35b9a3,#45c4ae 50%,#35b9a3)}

  .interviews{top:2109px;height:499px;background:var(--white)}
  .interviews .heading{top:56px;font-size:38px;color:var(--sky);font-weight:400}
  .interviews .people{left:129px;top:157px}
  .finalist{position:absolute;left:891px;top:157px}
  .arrow{position:absolute;left:775px;top:218px}
  .interviews .btn-interviews{left:342px;top:397px;width:140px;height:39px;background:var(--dark)}
  .interviews .btn-finalist{left:916px;top:397px;width:143px;height:39px;background:var(--teal)}

  .training{top:2608px;height:350px;background:var(--teal)}
  .training-title{position:absolute;left:198px;top:90px;font-family:"Montserrat",Arial,sans-serif;font-weight:400;font-size:39px;line-height:46px;color:var(--white)}
  .training .btn{left:198px;top:242px;width:141px;height:39px;background:var(--dark);text-transform:none;font-size:12px}
  .training-art{position:absolute;left:612px;top:62px;width:392px;height:231px;border-radius:8px;background:linear-gradient(135deg,#4fc6b3,#2aa693)}

  .start{top:2958px;height:153px;background:var(--white)}
  .start .btn{left:494px;top:35px;width:212px;height:62px;background:var(--sky);font-family:"Montserrat",Arial,sans-serif;font-size:28px;text-transform:uppercase;letter-spacing:0}

  .support{top:3111px;background:var(--sky-band)}
  .support .band-art{background:linear-gradient(90deg,#86c9e3,#99d4ea 50%,#86c9e3)}

  .site-footer{top:3323px;height:139px;background:var(--white);text-align:center}
  .footer-nav{position:absolute;top:40px;left:0;width:1200px;font-size:12.5px;color:var(--ink)}
  .footer-nav span{margin:0 6px}
  .copyright{position:absolute;top:82px;left:0;width:1200px;font-size:12.5px;color:var(--ink)}
</style>
</head>
<body>

<header class="section site-header">
  <div class="brand"><span class="brand-square"></span>BrindleCare</div>
  <svg class="menu-icon" width="26" height="22" viewBox="0 0 26 22" aria-hidden="true">
    <rect y="1" width="26" height="4" fill="#2fb6a2"/><rect y="9" width="26" height="4" fill="#2fb6a2"/><rect y="17" width="26" height="4" fill="#2fb6a2"/>
  </svg>
</header>

<section class="section hero">
  <h1 class="hero-title">BrindleCARE</h1>
  <p class="hero-text">Neque porro quisquam est qui dolorem ipsum quia dolor sit amet, consectetur, adipisci velit.</p>
  <div class="btn">Learn More</div>
  <div class="hero-art" role="img" aria-label="Illustration of a businessman presenting a bar chart on a computer monitor"></div>
  <div class="dots"><span></span><span></span><span></span><span></span></div>
</section>

<section class="section pool">
  <div class="people">
    <div class="person"><div class="photo" role="img" aria-label="Candidate portrait"></div><p class="person-name">Daniel Foster</p></div>
    <div class="person"><div class="photo" role="img" aria-label="Candidate portrait"></div><p class="person-name">Daniel Foster</p></div>
    <div class="person"><div class="photo" role="img" aria-label="Candidate portrait"></div><p class="person-name">Daniel Foster</p></div>
    <div class="person"><div class="photo" role="img" aria-label="Candidate portrait"></div><p class="person-name">Daniel Foster</p></div>
    <div class="person"><div class="photo" role="img" aria-label="Candidate portrait"></div><p class="person-name">Daniel Foster</p></div>
  </div>
  <h2 class="heading">Collect and Synthesize<br>Candidates for Training, Employment</h2>
</section>

<section class="section summary">
  <div class="summary-art" role="img" aria-label="Faint background illustration of business icons and a handshake"></div>
  <h2 class="heading">Summary For Employer</h2>
  <p class="summary-text">Lorem Ipsum is simply dummy text of the printing and typesetting industry. Lorem Ipsum has been the industry's standard dummy text ever since the 1500s, when an unknown printer took a galley of type and scrambled it to make a type specimen book. It has survived not only five centuries, but also the leap into electronic typesetting, remaining essentially unchanged.</p>
  <div class="btn">Learn More</div>
</section>

<section class="section selection">
  <h2 class="heading">Employer selects their favored<br>candidates to interview</h2>
  <div class="people">
    <div class="person"><div class="photo" role="img" aria-label="Candidate portrait"></div><p class="person-name">Daniel Foster</p></div>
    <div class="person"><div class="photo" role="img" aria-label="Candidate portrait"></div><p class="person-name">Daniel Foster</p></div>
    <div class="person"><div class="photo" role="img" aria-label="Candidate portrait"></div><p class="person-name">Daniel Foster</p></div>
    <div class="person"><div class="photo" role="img" aria-label="Candidate portrait"></div><p class="person-name">Daniel Foster</p></div>
    <div class="person"><div class="photo" role="img" aria-label="Candidate portrait"></div><p class="person-name">Daniel Foster</p></div>
  </div>
</section>

<section class="section band protocol">
  <div class="band-art" role="img" aria-label="Faint pattern of business and finance icons"></div>
  <h2 class="heading">Employer, BrindleCare agree upon training protocol</h2>
</section>

<section class="section interviews">
  <h2 class="heading">Candidates interviewed by Employer</h2>
  <div class="people">
    <div class="person"><div class="photo" role="img" aria-label="Candidate portrait"></div><p class="person-name">Daniel Foster</p></div>
    <div class="person"><div class="photo" role="img" aria-label="Candidate portrait"></div><p class="person-name">Daniel Foster</p></div>
    <div class="person"><div class="photo" role="img" aria-label="Candidate portrait"></div><p class="person-name">Daniel Foster</p></div>
  </div>
  <svg class="arrow" width="34" height="30" viewBox="0 0 34 30" aria-hidden="true">
    <path d="M2 15 H28 M18 4 L30 15 L18 26" fill="none" stroke="#2fb6a2" stroke-width="6" stroke-linecap="square"/>
  </svg>
  <div class="person finalist"><div class="photo" role="img" aria-label="Finalist candidate portrait"></div><p class="person-name">Daniel Foster</p></div>
  <div class="btn btn-interviews">Interviews</div>
  <div class="btn btn-finalist">Finalist</div>
</section>

<section class="section training">
  <h2 class="training-title">BRINDLECARE<br>PRE-EMPLOYMENT<br>TRAINING</h2>
  <div class="btn">LEARN MORE</div>
  <div class="training-art" role="img" aria-label="Illustration of two people shaking hands through computer screens"></div>
</section>

<section class="section start">
  <div class="btn">Start Job</div>
</section>

<section class="section band support">
  <div class="band-art" role="img" aria-label="Faint pattern of business and finance icons"></div>
  <h2 class="heading">Post Employment Support (1-3 months)</h2>
</section>

<footer class="section site-footer">
  <nav class="footer-nav">Home<span>|</span>Employers<span>|</span>Nurse Practitioners and Physician Assistants<span>|</span>Medical Specialties<span>|</span>Contact</nav>
  <p class="copyright">© 2015 Company Name | All Rights Reserved</p>
</footer>

</body>
</html>
```